Sumvera financial services stationery design

We need business stationery designed with letterheads, business cards, with compliments and envelope for a business that offers tax and accounting services
Updates

Designs look the same

Target Market(s)

Small to medium businesses, individuals, Self managed superfunds

Industry/Entity Type

Business

Font styles to use
Serif
Other font styles liked:
• Atlanta

Colors
32a6d6
3277b5

Requirements
Must have
• Logo incorporated with all my stationery
• professional
Should not have
• Lots of colours
• Busy

```html
<!DOCTYPE html>
<html lang="en">
<head>
<meta charset="utf-8">
<title>Sumvera Financial Services – Business Card</title>
<link rel="stylesheet" href="https://fonts.googleapis.com/css2?family=Questrial&display=swap">
<style>
  :root {
    --brand-blue: #206bad;
    --brand-sky: #32a6d6;
    --ink: #2b2b2b;
    --ink-soft: #4a4a4a;
    --steel: #a9adb1;
    --paper: #f7f7f7;
    --backdrop: #e6e6e8;
  }
  * { box-sizing: border-box; margin: 0; padding: 0; }
  html, body { width: 1200px; height: 1200px; overflow: hidden; }
  body {
    background: var(--backdrop);
    font-family: "Questrial", "Century Gothic", sans-serif;
    color: var(--ink);
    position: relative;
  }
  .card {
    position: absolute;
    left: 180px;
    width: 840px;
    height: 480px;
    box-shadow: 0 10px 30px rgba(0,0,0,0.12);
  }
  .card--front { top: 70px; background: var(--brand-blue); display: flex; align-items: center; justify-content: center; }
  .card--back { top: 650px; background: var(--paper); }

  .wordmark { display: flex; align-items: center; gap: 16px; }
  .wordmark__square { width: 46px; height: 46px; background: var(--brand-sky); }
  .wordmark__name { font-size: 58px; letter-spacing: 2px; text-transform: uppercase; }
  .card--front .wordmark__name { color: var(--steel); }
  .card--back .wordmark { position: absolute; left: 80px; top: 170px; }
  .card--back .wordmark__square { background: var(--brand-blue); }
  .card--back .wordmark__name { color: var(--ink-soft); font-size: 52px; }

  .holder { position: absolute; right: 60px; top: 52px; text-align: right; }
  .holder__name { font-size: 32px; font-weight: 700; color: var(--ink-soft); -webkit-text-stroke: 0.6px var(--ink-soft); }
  .holder__role { font-size: 26px; color: var(--ink); margin-top: 2px; }

  .contacts { position: absolute; font-size: 22px; line-height: 32px; }
  .contacts li { list-style: none; display: flex; align-items: center; gap: 12px; }
  .contacts svg { width: 18px; height: 18px; fill: var(--ink-soft); }
  .contacts--phone { left: 80px; top: 282px; }
  .contacts--web { left: 460px; top: 250px; }
  .address { position: absolute; left: 80px; top: 360px; font-size: 23px; }
  .band { position: absolute; left: 0; bottom: 18px; width: 840px; height: 44px; }
</style>
</head>
<body>
  <section class="card card--front" aria-label="Business card front">
    <div class="wordmark">
      <span class="wordmark__square"></span>
      <span class="wordmark__name">Sumvera</span>
    </div>
  </section>

  <section class="card card--back" aria-label="Business card back">
    <div class="holder">
      <p class="holder__name">Daniel Hartley</p>
      <p class="holder__role">Director &amp; CEO</p>
    </div>

    <div class="wordmark">
      <span class="wordmark__square"></span>
      <span class="wordmark__name">Sumvera</span>
    </div>

    <ul class="contacts contacts--phone">
      <li><svg viewBox="0 0 24 24"><path d="M6.6 10.8a15 15 0 0 0 6.6 6.6l2.2-2.2c.3-.3.7-.4 1-.2 1.1.4 2.3.6 3.6.6.6 0 1 .4 1 1V20c0 .6-.4 1-1 1A17 17 0 0 1 3 4c0-.6.4-1 1-1h3.5c.6 0 1 .4 1 1 0 1.3.2 2.5.6 3.6.1.3 0 .7-.2 1z"/></svg>555.210.4837</li>
      <li><svg viewBox="0 0 24 24"><path d="M7 1h10a2 2 0 0 1 2 2v18a2 2 0 0 1-2 2H7a2 2 0 0 1-2-2V3a2 2 0 0 1 2-2zm0 3v15h10V4zm5 16.2a.9.9 0 1 0 0 1.8.9.9 0 0 0 0-1.8z"/></svg>555.384.9012</li>
    </ul>

    <ul class="contacts contacts--web">
      <li><svg viewBox="0 0 24 24"><path d="M2 5h20v14H2zm2 2v.4l8 5.2 8-5.2V7zm0 2.8V17h16V9.8l-8 5.2z"/></svg>hello@sumvera.com</li>
      <li><svg viewBox="0 0 24 24"><path d="M12 2a10 10 0 1 0 0 20 10 10 0 0 0 0-20zm6.9 9h-3a15 15 0 0 0-1.3-5.6A8 8 0 0 1 18.9 11zM12 4c.9 1.2 1.8 3.6 1.9 7h-3.8c.1-3.4 1-5.8 1.9-7zM9.4 5.4A15 15 0 0 0 8.1 11h-3a8 8 0 0 1 4.3-5.6zM5.1 13h3a15 15 0 0 0 1.3 5.6A8 8 0 0 1 5.1 13zM12 20c-.9-1.2-1.8-3.6-1.9-7h3.8c-.1 3.4-1 5.8-1.9 7zm2.6-1.4a15 15 0 0 0 1.3-5.6h3a8 8 0 0 1-4.3 5.6z"/></svg>www.sumvera.com</li>
    </ul>

    <p class="address">18 Harbour Lane, Brookfield, NY 10234</p>

    <svg class="band" viewBox="0 0 840 44" preserveAspectRatio="none" aria-hidden="true">
      <polygon points="0,0 700,0 744,44 0,44" fill="var(--brand-blue)"/>
      <polygon points="712,0 840,0 840,44 756,44" fill="var(--steel)"/>
    </svg>
  </section>
</body>
</html>
```